i would like a business card to leave with customers and potential customers for electrical work and for the supply and install of reverse cycle airconditioning in the domestic and commercial market.
I own my own business and im a sole trader. I have an a'class electrical lisence and also a refrigeration lisence so i am
able to offer complete installations in airconditioning by a fully qualified and lisenced tradesman.
im looking for something that comes across as unique and professional.
i had the coluor black and some gold in mind but open to any coluors.
something like Beacon Electrical & Refrigeration
or Beacon Air.
i will use this design on a business card to advertise through summer to help generate installs through the busy season.

Target Market(s)

Mainly domestic house holds through summer who are in need of airconditioning and reliable information to acomadate thier cooling and heating requirements

Industry/Entity Type

Electrical

Requirements
Must have
• Business name- Beacon
My name- Peter Wollaston
My mobile no- 0457 819 302
My email- prwollaston@tarvel.com.au
Installation & Decomissioning of aiconditioning split systems
LIC NO: KTR 407516
Nice to have
• Beacon Electrical & Refrigeration

```html
<!DOCTYPE html>
<html lang="en">
<head>
<meta charset="utf-8">
<title>Beacon Electrical &amp; Refrigeration – Business Card</title>
<link rel="stylesheet" href="https://fonts.googleapis.com/css2?family=Raleway:wght@400;500;600&family=Arimo:wght@400&display=swap">
<style>
  :root {
    --page: #ffffff;
    --card: #ffffff;
    --card-edge: #8c8c8c;
    --mark-grey: #6f6f6f;
    --ink: #2b2b2b;
    --ink-soft: #4a4a4a;
    --band: #8b8b8b;
    --band-text: #ffffff;
    --accent-blue: #2a9fd8;
    --badge: #3fa6d9;
  }
  * { margin: 0; padding: 0; box-sizing: border-box; }
  html, body {
    width: 1200px; height: 850px; overflow: hidden;
    background: var(--page);
  }
  .canvas { position: relative; width: 1200px; height: 850px; }

  .card {
    position: absolute; left: 309px; width: 602px; height: 346px;
    background: var(--card);
    border: 1px solid var(--card-edge);
    border-radius: 10px;
  }
  .card--front { top: 45px; }
  .card--back { top: 437px; }

  .brand { position: absolute; color: var(--mark-grey); font-family: "Raleway", sans-serif; font-weight: 600; text-align: center; }
  .brand__name { display: block; line-height: 1; letter-spacing: -2px; }
  .brand__line { display: block; font-family: "Arimo", sans-serif; font-weight: 400; color: var(--ink); }

  .card--front .brand { left: 110px; top: 58px; width: 374px; }
  .card--front .brand__name { font-size: 122px; }
  .card--front .brand__line { font-size: 20px; margin-top: 34px; letter-spacing: -0.1px; }

  .badge {
    position: absolute; left: 208px; top: 278px;
    width: 40px; height: 40px; background: var(--badge);
  }

  .name-band {
    position: absolute; left: 0; top: 64px; width: 286px; height: 31px;
    background: var(--band); color: var(--band-text);
    font-family: "Raleway", sans-serif; font-size: 22px; font-weight: 400;
    padding-left: 63px; line-height: 31px;
  }
  .service {
    position: absolute; left: 61px; top: 110px;
    font-family: "Raleway", sans-serif; font-size: 14.5px; line-height: 19px;
    color: var(--ink-soft);
  }
  .licence {
    position: absolute; left: 61px; top: 183px;
    font-family: "Raleway", sans-serif; font-size: 12px; color: var(--ink-soft);
  }
  .contact {
    position: absolute; left: 26px; top: 237px; list-style: none;
    font-family: "Raleway", sans-serif; font-size: 15.5px; color: var(--ink);
  }
  .contact li { display: flex; align-items: center; height: 25px; }
  .contact svg { width: 26px; height: 18px; margin-right: 10px; }

  .card--back .brand { left: 355px; top: 98px; width: 212px; }
  .card--back .brand__name { font-size: 68px; letter-spacing: -1px; }
  .card--back .brand__line { font-size: 11.5px; margin-top: 14px; }
</style>
</head>
<body>
<main class="canvas">
  <section class="card card--front" aria-label="Card front">
    <div class="brand">
      <span class="brand__name">Beacon</span>
      <span class="brand__line">Beacon Electrical &amp; Refrigeration</span>
    </div>
    <div class="badge" role="img" aria-label="Authorised dealer badge"></div>
  </section>

  <section class="card card--back" aria-label="Card back">
    <div class="name-band">Peter Wollaston</div>
    <p class="service">Installation &amp; Decomissioning<br>of aiconditioning split systems</p>
    <p class="licence">LIC NO: KTR 407516</p>
    <ul class="contact">
      <li>
        <svg viewBox="0 0 26 18" aria-hidden="true">
          <path d="M2 6 Q13 -1 24 6 L21 9 L18 6.5 L8 6.5 L5 9 Z" fill="var(--accent-blue)"/>
          <path d="M8 8 L18 8 L22 16 L4 16 Z" fill="var(--accent-blue)"/>
          <circle cx="13" cy="12" r="2.4" fill="#fff"/>
        </svg>
        0457 819 302
      </li>
      <li>
        <svg viewBox="0 0 26 18" aria-hidden="true">
          <rect x="3" y="3" width="20" height="13" fill="none" stroke="var(--accent-blue)" stroke-width="1.3"/>
          <path d="M3 3 L13 11 L23 3 M3 16 L10 9 M23 16 L16 9" fill="none" stroke="var(--accent-blue)" stroke-width="1.3"/>
        </svg>
        prwollaston@tarvel.com.au
      </li>
    </ul>
    <div class="brand">
      <span class="brand__name">Beacon</span>
      <span class="brand__line">Beacon Electrical &amp; Refrigeration</span>
    </div>
  </section>
</main>
</body>
</html>
```